Our Crooked Plot: Need a label for bee and garden related products

We want to distribute some homemade goods from our bees and greenhouse garden to friends, family, and neighbors. Things like honey, beeswax candles, lip balm, tomato sauce, pickles, etc. The yard itself is also a bit odd as it's almost an acre, but it's really long and narrow. We'd like to call it "Our Crooked Plot". We're open to a variety of designs and really don't have specific preferences just yet.

Font styles to use
Serif
Decorative
Script

Requirements
Must have
• The company name, Our Crooked Plot.

```html
<!DOCTYPE html>
<html lang="en">
<head>
<meta charset="utf-8">
<title>Our Crooked Plot – Label Samples</title>
<link rel="stylesheet" href="https://fonts.googleapis.com/css2?family=Josefin+Sans:wght@600;700&family=Playfair+Display:wght@700&display=swap">
<style>
  :root {
    --paper: #ffffff;
    --navy-deep: #0b1a22;
    --navy-mid: #294350;
    --gold: #b8913f;
    --gold-soft: #c9a55a;
    --ink-light: #f1f1ee;
    --caption: #13294b;
  }
  html, body {
    margin: 0;
    padding: 0;
    overflow: hidden;
    background: var(--paper);
  }
  .canvas {
    position: relative;
    width: 1200px;
    height: 926px;
    background: var(--paper);
    overflow: hidden;
  }
  .label {
    position: absolute;
    top: 322px;
    width: 362px;
    height: 362px;
  }
  .label--one { left: 146px; }
  .label--two { left: 678px; }
  .arc-text {
    font-family: "Josefin Sans", sans-serif;
    font-weight: 700;
    font-size: 15px;
    letter-spacing: 3px;
    fill: var(--ink-light);
  }
  .brand-name {
    font-family: "Playfair Display", serif;
    font-weight: 700;
    fill: var(--ink-light);
    text-anchor: middle;
  }
  .caption {
    position: absolute;
    top: 856px;
    width: 300px;
    margin: 0;
    text-align: center;
    font-family: "Josefin Sans", sans-serif;
    font-weight: 700;
    font-size: 27px;
    letter-spacing: 2px;
    color: var(--caption);
  }
  .caption--one { left: 177px; }
  .caption--two { left: 709px; }
</style>
</head>
<body>
<main class="canvas">

  <svg class="label label--one" viewBox="0 0 400 400" aria-label="Label sample one">
    <defs>
      <radialGradient id="face-one" cx="40%" cy="45%" r="65%">
        <stop offset="0" stop-color="var(--navy-mid)"/>
        <stop offset="1" stop-color="var(--navy-deep)"/>
      </radialGradient>
      <path id="arc-top-one" d="M 62 200 A 138 138 0 0 1 338 200"/>
      <path id="arc-bottom-one" d="M 55 200 A 145 145 0 0 0 345 200"/>
    </defs>
    <circle cx="200" cy="200" r="200" fill="url(#face-one)"/>
    <circle cx="200" cy="200" r="192" fill="none" stroke="var(--gold)" stroke-width="1.2"/>
    <circle class="braid-band" cx="200" cy="200" r="179" fill="none" stroke="var(--gold)" stroke-width="17" role="img" aria-label="Gold chevron braid border"/>
    <circle cx="200" cy="200" r="165" fill="none" stroke="var(--gold)" stroke-width="1.6" stroke-dasharray="1.5 3.5"/>
    <circle cx="200" cy="200" r="159" fill="none" stroke="var(--gold)" stroke-width="1"/>
    <text class="arc-text"><textPath href="#arc-top-one" startOffset="50%" text-anchor="middle">100% BEESWAX CANDLES</textPath></text>
    <rect x="178" y="88" width="44" height="44" rx="8" fill="var(--gold)" role="img" aria-label="Honey bee illustration"/>
    <text class="brand-name" x="200" y="200" font-size="40">OUR CROOKED</text>
    <text class="brand-name" x="200" y="248" font-size="40">PLOT</text>
    <rect x="140" y="280" width="120" height="24" rx="4" fill="var(--gold)" opacity="0.8" role="img" aria-label="Gold scroll ornament"/>
    <text class="arc-text"><textPath href="#arc-bottom-one" startOffset="50%" text-anchor="middle">NATURAL HEALTH PRODUCTS</textPath></text>
  </svg>

  <svg class="label label--two" viewBox="0 0 400 400" aria-label="Label sample two">
    <defs>
      <radialGradient id="face-two" cx="40%" cy="45%" r="65%">
        <stop offset="0" stop-color="var(--navy-mid)"/>
        <stop offset="1" stop-color="var(--navy-deep)"/>
      </radialGradient>
      <path id="arc-top-two" d="M 42 200 A 158 158 0 0 1 358 200"/>
      <path id="arc-bottom-two" d="M 36 200 A 164 164 0 0 0 364 200"/>
    </defs>
    <circle cx="200" cy="200" r="200" fill="url(#face-two)"/>
    <circle cx="200" cy="200" r="191" fill="none" stroke="var(--gold)" stroke-width="1.2"/>
    <circle cx="200" cy="200" r="185" fill="none" stroke="var(--gold)" stroke-width="1.6" stroke-dasharray="1.5 3.5"/>
    <text class="arc-text"><textPath href="#arc-top-two" startOffset="50%" text-anchor="middle">100% BEESWAX CANDLES</textPath></text>
    <rect x="174" y="70" width="52" height="52" rx="9" fill="var(--gold)" role="img" aria-label="Honey bee illustration"/>
    <text class="brand-name" x="200" y="196" font-size="48">OUR CROOKED</text>
    <text class="brand-name" x="200" y="252" font-size="48">PLOT</text>
    <rect x="130" y="288" width="140" height="28" rx="4" fill="var(--gold)" opacity="0.8" role="img" aria-label="Gold scroll ornament"/>
    <text class="arc-text"><textPath href="#arc-bottom-two" startOffset="50%" text-anchor="middle">NATURAL HEALTH PRODUCTS</textPath></text>
  </svg>

  <p class="caption caption--one">SAMPLE ONE</p>
  <p class="caption caption--two">SAMPLE TWO</p>

</main>
</body>
</html>
```